Business Cards and Company profile

I already have a company logo and website, I really need someone to come up with designs that are inkeeping with the theme of the website and the logo.
I need business cards and the company profile reworked (I areadly have the text) as described above.

thanks
Gareth
drifthavenvoyages.example

Target Market(s)

Mainly be for travel trade facing.

Industry/Entity Type

Business

```html
<!DOCTYPE html>
<html lang="en">
<head>
<meta charset="utf-8">
<title>Drifthaven Voyages – Business Cards</title>
<link href="https://fonts.googleapis.com/css2?family=Open+Sans:wght@400;600;700;800&display=swap" rel="stylesheet">
<style>
  :root {
    --backdrop-light: #a9a9a9;
    --backdrop-dark: #7c7c7c;
    --brand-yellow: #e8c01c;
    --ink-dark: #2f2f2f;
    --ink-mid: #555a5e;
    --band-dark: #303030;
    --card-white: #ffffff;
    --mist-blue: #dbe6ef;
    --sky-top: #3f74b8;
    --sky-low: #9fc0e0;
    --sea: #b9cfdd;
  }
  * { margin: 0; padding: 0; box-sizing: border-box; }
  html, body { width: 1200px; height: 597px; overflow: hidden; }
  body {
    position: relative;
    font-family: "Open Sans", sans-serif;
    background: radial-gradient(ellipse at 50% 60%, var(--backdrop-light), var(--backdrop-dark));
  }
  .card {
    position: absolute;
    top: 173px;
    width: 458px;
    height: 262px;
    border-radius: 14px;
    overflow: hidden;
    box-shadow: 0 2px 6px rgba(0,0,0,0.25);
  }
  .card--front { left: 121px; background: var(--card-white); }
  .card--back { left: 602px; }

  .front-photo {
    position: absolute; inset: 0;
    background:
      linear-gradient(90deg, rgba(255,255,255,0.9) 0%, rgba(255,255,255,0.2) 55%, rgba(255,255,255,0) 100%),
      linear-gradient(180deg, #eef3f8 0%, #f4f7fa 40%, var(--mist-blue) 70%, #e9f0f5 100%);
  }
  .holder { position: absolute; right: 29px; top: 20px; text-align: right; }
  .holder__name { font-size: 16.5px; font-weight: 700; color: var(--ink-dark); line-height: 22px; }
  .holder__role { font-size: 13.5px; font-weight: 400; color: var(--ink-mid); line-height: 20px; letter-spacing: 0.3px; }

  .brand-name {
    position: absolute;
    font-weight: 800;
    color: var(--brand-yellow);
    letter-spacing: 0.4px;
    white-space: nowrap;
    display: flex; align-items: center; gap: 7px;
  }
  .brand-name__dot { width: 12px; height: 12px; border-radius: 50%; background: var(--brand-yellow); }
  .card--front .brand-name { left: 17px; top: 92px; font-size: 15.5px; }
  .card--back .brand-name { right: 24px; bottom: 22px; font-size: 14px; }

  .address { position: absolute; left: 23px; top: 136px; font-size: 11.8px; line-height: 15px; color: var(--ink-mid); }
  .contacts { position: absolute; left: 23px; top: 179px; list-style: none; }
  .contacts li { display: flex; align-items: center; gap: 10px; font-size: 11.8px; line-height: 16.3px; color: var(--ink-mid); }
  .contacts svg { width: 13px; height: 11px; fill: var(--brand-yellow); flex: none; }

  .front-bands { position: absolute; left: 0; bottom: 0; width: 458px; height: 22px; }

  .back-photo {
    position: absolute; inset: 0;
    background: linear-gradient(180deg, var(--sky-top) 0%, var(--sky-low) 45%, #e3ecf3 63%, var(--sea) 68%, #dce6ee 85%, #f3f6f9 100%);
  }
</style>
</head>
<body>
  <section class="card card--front" aria-label="Business card front">
    <div class="front-photo" role="img" aria-label="Faded photo of a white cruise ship at sea"></div>
    <div class="holder">
      <p class="holder__name">Gareth Holloway</p>
      <p class="holder__role">Managing Director</p>
    </div>
    <div class="brand-name"><span class="brand-name__dot"></span>DRIFTHAVEN VOYAGES</div>
    <p class="address">Harbour Suite, 1st Floor, Marlow House,<br>212 Quayside Road, Essex, CM1 4QT</p>
    <ul class="contacts">
      <li><svg viewBox="0 0 13 11"><path d="M1 3c0-2 3-2.5 5.5-2.5S12 1 12 3v1.2H9.3V3H3.7v1.2H1z M2.5 5.5h8l1 5H1.5z"/></svg>01632 960 010</li>
      <li><svg viewBox="0 0 13 11"><path d="M3 0h7v3.5H3z M0.5 4h12v5h-2V7h-8v2h-2z M3 7.5h7V11H3z"/></svg>01632 960 019</li>
      <li><svg viewBox="0 0 13 11"><path d="M0.5 1h12v9h-12z M1.6 2l4.9 4 4.9-4v1.3L6.5 7.3 1.6 3.3z" fill-rule="evenodd"/></svg>admin@drifthavenvoyages.example</li>
      <li><svg viewBox="0 0 13 11"><path d="M6.5 0 13 5.5h-2V11H8V7.5H5V11H2V5.5H0z"/></svg>www.drifthavenvoyages.example</li>
    </ul>
    <svg class="front-bands" viewBox="0 0 458 22" preserveAspectRatio="none" aria-hidden="true">
      <polygon points="0,10 262,10 282,22 0,22" fill="var(--band-dark)"/>
      <polygon points="260,0 458,0 458,22 282,22" fill="var(--brand-yellow)"/>
      <polygon points="262,10 266,10 284,22 280,22" fill="#fff"/>
    </svg>
  </section>

  <section class="card card--back" aria-label="Business card back">
    <div class="back-photo" role="img" aria-label="Photo of a large white cruise ship on calm sea under a blue sky"></div>
    <div class="brand-name"><span class="brand-name__dot"></span>DRIFTHAVEN VOYAGES</div>
  </section>
</body>
</html>
```